Real Estate Valuation Services

format
A5 portrait, look at the picture
Double-sided: Front = visual & emotional, Back = informative & structured.
goal
Highlight the free hedonic property valuation as the main offer.
Build trust by presenting the company as an exclusive, family-owned real estate firm with local roots in Meilen/ZH.
Communicate the USP “Everything from one source” clearly – from valuation to notary support and tax guidance.
Target audience
Homeowners in the Lake Zurich region considering selling their property.
Clients who value exclusivity, professionalism, and personal service.
Design style
Modern, clean, elegant – plenty of white space. Look at the website: https://brunnhofwohnen.ch/
Tone: Professional, trustworthy, exclusive – not like a mass-market flyer.
If possible, the text should be in German. Contact details must be included:
info@brunnhofwohnen.ch
+41 77 562 18 04
Target Market(s)
property owner
Industry/Entity Type
real estate
Look and feel

```html
<!DOCTYPE html>
<html lang="de">
<head>
<meta charset="utf-8">
<title>Brunnhof Wohnen – Immobilienbewertung Flyer</title>
<link rel="stylesheet" href="https://fonts.googleapis.com/css2?family=Montserrat:ital,wght@0,600;0,700;1,700&family=Lato:wght@400;700&display=swap">
<style>
  :root {
    --backdrop: #2b2b2b;
    --paper: #ffffff;
    --ink: #1a1a1a;
    --green: #3aa845;
    --green-dark: #1f9a5a;
    --green-light: #7cc04a;
    --panel-dark: #1c1c1c;
    --card-border: #e3e3e3;
    --muted: #333333;
  }
  * { box-sizing: border-box; margin: 0; padding: 0; }
  html, body { width: 1200px; height: 1137px; overflow: hidden; background: var(--backdrop); }
  body { position: relative; font-family: "Lato", sans-serif; color: var(--ink); }

  .flyer { position: absolute; background: var(--paper); overflow: hidden; }
  .flyer--front { left: 52px; top: 86px; width: 523px; height: 733px; }
  .flyer--back  { left: 620px; top: 324px; width: 522px; height: 736px; }

  .brand {
    font-family: "Montserrat", sans-serif; font-weight: 700; color: var(--green);
    display: flex; align-items: center; gap: 10px; white-space: nowrap;
  }
  .brand__mark { width: 14px; height: 14px; background: var(--green); flex: none; }

  /* Front */
  .front__corner { position: absolute; right: 0; top: 0; }
  .front__brand { position: absolute; top: 54px; left: 0; right: 0; justify-content: center; font-size: 38px; }
  .front__headline {
    position: absolute; top: 136px; left: 0; right: 0; text-align: center;
    font-family: "Montserrat", sans-serif; font-weight: 700; font-size: 42px; line-height: 50px; color: var(--ink);
  }
  .front__rule {
    position: absolute; top: 241px; left: 50px; right: 50px; height: 2px;
    background: linear-gradient(90deg, var(--green-dark), var(--green-light));
  }
  .front__quote {
    position: absolute; top: 260px; left: 20px; right: 20px; text-align: center;
    font-family: "Montserrat", sans-serif; font-style: italic; font-weight: 700; font-size: 20px; line-height: 28px;
    color: var(--green);
  }
  .front__landscape {
    position: absolute; left: 0; right: 0; top: 459px; bottom: 0;
    background: linear-gradient(180deg, #7fdc8c 0%, #3fb86a 55%, #27a862 100%);
  }
  .front__portrait {
    position: absolute; left: 76px; top: 338px; width: 366px; height: 395px;
    background: linear-gradient(180deg, #c9a48a 0%, #8d6a55 45%, #2a2a2e 75%, #1e1e22 100%);
    border-radius: 160px 160px 0 0;
  }
  .front__cut { position: absolute; left: 0; bottom: 0; }

  /* Back */
  .back__photo {
    position: absolute; left: 0; top: 0; width: 100%; height: 279px;
    background: linear-gradient(180deg, #bdf7ff 0%, #a9f27a 45%, #5fd14a 100%);
  }
  .back__intro {
    position: absolute; left: 28px; top: 205px; width: 467px; height: 174px;
    background: var(--panel-dark); border-bottom: 2px solid var(--green); padding: 16px 18px;
  }
  .back__title {
    font-family: "Montserrat", sans-serif; font-weight: 700; font-size: 19px; line-height: 24px;
    text-align: center; color: var(--green-light);
  }
  .back__title span { display: block; color: var(--green); }
  .back__intro-rule { height: 1px; background: var(--green); margin: 9px 0 10px; opacity: .8; }
  .back__intro-text { font-size: 14px; line-height: 17px; color: #fff; text-align: justify; }

  .services { position: absolute; left: 30px; top: 401px; display: flex; gap: 10px; }
  .service {
    position: relative; width: 147px; height: 150px; border: 1px solid var(--card-border);
    box-shadow: 0 2px 5px rgba(0,0,0,.12); text-align: center; padding-top: 14px;
  }
  .service__name { font-family: "Montserrat", sans-serif; font-weight: 700; font-size: 17px; color: var(--green-dark); }
  .service__text { font-size: 11.5px; line-height: 14px; color: var(--muted); margin-top: 6px; }
  .service__icon { position: absolute; right: 14px; bottom: 10px; }

  .cta {
    position: absolute; left: 35px; top: 571px; width: 457px; height: 67px;
    background: linear-gradient(90deg, var(--green-dark), var(--green-light));
    display: flex; align-items: center; justify-content: center; text-align: center;
    font-family: "Montserrat", sans-serif; font-weight: 700; font-size: 16px; line-height: 21px; color: #fff;
  }

  .back__brand { position: absolute; left: 62px; top: 678px; font-size: 19px; line-height: 24px; gap: 8px; }
  .back__brand .brand__mark { width: 12px; height: 12px; }
  .contact { position: absolute; left: 282px; top: 664px; list-style: none; font-size: 13px; line-height: 18px; color: var(--ink); }
  .contact li { display: flex; align-items: center; gap: 7px; white-space: nowrap; }
  .contact svg { flex: none; }
</style>
</head>
<body>

<section class="flyer flyer--front" aria-label="Flyer Vorderseite">
  <svg class="front__corner" width="98" height="98" viewBox="0 0 98 98" aria-hidden="true">
    <polygon points="0,0 98,0 98,98" fill="#7cc04a"/>
  </svg>
  <div class="brand front__brand"><span class="brand__mark"></span>Brunnhof Wohnen</div>
  <h1 class="front__headline">Ihre Immobilie.<br>Unser Versprechen.</h1>
  <div class="front__rule"></div>
  <p class="front__quote">„Kostenlose und exklusive<br>Immobilienbewertung am Zürichsee.“</p>
  <div class="front__landscape" role="img" aria-label="Grün getönte Ansicht der Häuser am Zürichsee"></div>
  <div class="front__portrait" role="img" aria-label="Porträt der Ansprechpartnerin im dunklen Blazer"></div>
  <svg class="front__cut" width="102" height="102" viewBox="0 0 102 102" aria-hidden="true">
    <polygon points="0,0 102,102 0,102" fill="#ffffff"/>
  </svg>
</section>

<section class="flyer flyer--back" aria-label="Flyer Rückseite">
  <div class="back__photo" role="img" aria-label="Grün getönter Blick von einer Terrasse über Wohnhäuser am Zürichsee"></div>

  <div class="back__intro">
    <h2 class="back__title">Kostenlose Immobilienbewertung<span>exklusiv für Eigentümer am Zürichsee</span></h2>
    <div class="back__intro-rule"></div>
    <p class="back__intro-text">„Wir sind ein familiengeführtes Immobilienunternehmen aus Meilen. Mit persönlicher Betreuung und diskretem Service begleiten wir Sie – von der ersten Bewertung bis hin zu Notar- und Steuerfragen.“</p>
  </div>

  <div class="services">
    <article class="service">
      <h3 class="service__name">Bewertung</h3>
      <p class="service__text">Marktgerechte<br>Wertermittlung</p>
      <svg class="service__icon" width="40" height="36" viewBox="0 0 40 36" fill="none" stroke="#1f9a5a" stroke-width="2.4" stroke-linejoin="round" aria-hidden="true">
        <path d="M3 17 L18 4 L33 17"/><path d="M7 14 V32 H22"/><circle cx="29" cy="26" r="7"/><path d="M29 22 V30"/>
      </svg>
    </article>
    <article class="service">
      <h3 class="service__name">Verkauf</h3>
      <p class="service__text">Exklusive<br>Vermarktung<br>&amp; Beratung</p>
      <svg class="service__icon" width="40" height="36" viewBox="0 0 40 36" fill="none" stroke="#1f9a5a" stroke-width="2.4" stroke-linejoin="round" stroke-linecap="round" aria-hidden="true">
        <path d="M2 18 L10 14 L20 22 L28 16 L38 20"/><path d="M10 14 L16 26 L22 30 L30 24"/><rect x="22" y="3" width="12" height="8"/>
      </svg>
    </article>
    <article class="service">
      <h3 class="service__name">Begleitung</h3>
      <p class="service__text">Alles aus einer Hand:<br>Notar &amp; Steuer</p>
      <svg class="service__icon" width="42" height="36" viewBox="0 0 42 36" fill="none" stroke="#1f9a5a" stroke-width="2.4" stroke-linecap="round" aria-hidden="true">
        <circle cx="21" cy="16" r="8"/><circle cx="21" cy="16" r="3"/>
        <path d="M21 3 V6 M21 26 V29 M8 16 H11 M31 16 H34 M12 7 L14 9 M28 23 L30 25 M30 7 L28 9 M12 25 L14 23"/>
        <path d="M4 33 L14 27 M38 33 L28 27"/>
      </svg>
    </article>
  </div>

  <div class="cta">„FORDERN SIE JETZT IHRE KOSTENLOSE<br>IMMOBILIENBEWERTUNG AN!“</div>

  <div class="brand back__brand"><span class="brand__mark"></span>Brunnhof Wohnen</div>
  <ul class="contact">
    <li><svg width="11" height="9" viewBox="0 0 11 9" aria-hidden="true"><rect x="0.5" y="0.5" width="10" height="8" fill="#1f9a5a"/><path d="M0.5 0.5 L5.5 5 L10.5 0.5" stroke="#fff" fill="none"/></svg>info@brunnhofwohnen.ch</li>
    <li><svg width="11" height="11" viewBox="0 0 11 11" aria-hidden="true"><path d="M2 0.5 L4 3 L3 4.5 Q4.5 7 6.5 8 L8 7 L10.5 9 L9 10.5 Q3 10 0.5 2 Z" fill="#1f9a5a"/></svg>+41 77 562 18 04</li>
    <li><svg width="11" height="11" viewBox="0 0 11 11" aria-hidden="true"><circle cx="5.5" cy="5.5" r="5" fill="#1f9a5a"/><path d="M0.5 5.5 H10.5 M5.5 0.5 Q2.5 5.5 5.5 10.5 Q8.5 5.5 5.5 0.5" stroke="#fff" stroke-width="0.8" fill="none"/></svg>brunnhofwohnen.ch</li>
  </ul>
</section>

</body>
</html>
```